Stationery and Logo Design Project for new NZ Accounting Firm

Our company name is based in Auckland, New Zealand and is called TMV CA Limited. We are a chartered accountancy firm hence the CA abbreviations.

We need a full logo stationery design: Logo, Letterhead, Business Card and Compliments slip.

We are looking for a bold, modern and clean/simple design that makes us stand out. We want to stand out as professionals in the industry and would like the logo and stationery that our clients see to convey this image. We also want to break away from the traditional boring views of book/bean accountants. We are not doing the same old things others are doing and are mainly cloud based but with face to face business relationship focused as well.

We see ourselves as business advisers that provide more than just filing their tax returns. We want to add value to their business and be a partner in their business ventures.

We want the logo to convey the above and also attract potential clients when they see our ads among the thousands on zarvo and the tallow index.

The logo can be for the "TMV" with CA Ltd seperately or a logo/design beside the TMV. But open to other suggestions or concept.

Hi Designers

The designs I have received so far is not quite what I want.

I want something modern and bold that is DIFFERENT from others, from the usual logo designs. Some logo that when people look at it they will remember it as opposed to fading in the background of other competitors' logo.

Lower case lettering for the TMV could be something to explore as I have not seen a lot of these and they do appeal to me.

Thanks

We can focus on the logo first as that will form the main part for all stationery.

Reason: Final stages of choosing a logo design so need to time for designers to submit the letterhead, namecards designs.

Target Market(s)

Our target clients are small to medium business ranging from the sole trader to 50 employees businesses

Industry/Entity Type

Business

```html
<!DOCTYPE html>
<html lang="en">
<head>
<meta charset="utf-8">
<title>TMV — Letterhead</title>
<link rel="stylesheet" href="https://fonts.googleapis.com/css2?family=Marcellus+SC&display=swap">
<style>
  :root {
    --accent: #f7890f;
    --charcoal: #333333;
    --ink: #111111;
    --paper: #ffffff;
  }
  html, body {
    margin: 0;
    padding: 0;
    overflow: hidden;
    background: var(--paper);
  }
  .letterhead {
    position: relative;
    width: 848px;
    height: 1200px;
    overflow: hidden;
    background: var(--paper);
    font-family: "Marcellus SC", "Times New Roman", serif;
    color: var(--ink);
  }
  .top-band {
    position: absolute;
    left: 0; top: 0;
    width: 100%;
    height: 11px;
    background: var(--accent);
  }
  .brand {
    position: absolute;
    left: 0; top: 18px;
    width: 100%;
    text-align: center;
  }
  .brand-name {
    margin: 0;
    font-size: 100px;
    line-height: 110px;
    font-weight: 400;
    letter-spacing: 4px;
    color: var(--charcoal);
  }
  .brand-tagline {
    margin: 12px 0 0;
    font-size: 16.5px;
    line-height: 20px;
  }
  .subject {
    position: absolute;
    left: 57px; top: 222px;
    margin: 0;
    font-size: 21px;
    line-height: 26px;
    font-weight: 400;
  }
  .letter-body {
    position: absolute;
    left: 51px; top: 287px;
    width: 746px;
    font-size: 15.8px;
    line-height: 17.9px;
    text-align: justify;
  }
  .letter-body p {
    margin: 0 0 9px;
  }
  .signoff {
    position: absolute;
    left: 51px; top: 866px;
    width: 320px;
    margin: 0;
    font-size: 16.5px;
    line-height: 20px;
  }
  .footer-note {
    position: absolute;
    left: 51px; top: 1092px;
    margin: 0;
    font-size: 11.5px;
    line-height: 15px;
    text-transform: uppercase;
  }
  .bottom-band {
    position: absolute;
    left: 0; bottom: 0;
    width: 100%;
    height: 40px;
    background: var(--charcoal);
  }
</style>
</head>
<body>
<main class="letterhead">
  <div class="top-band"></div>

  <header class="brand">
    <h1 class="brand-name">TMV</h1>
    <p class="brand-tagline">Dio dolorem sum diti quatur am que</p>
  </header>

  <h2 class="subject">Dio dolorem</h2>

  <section class="letter-body">
    <p>Ut dolut et autem dolupicia qui id eosandae in repta que cum etur reptat rerchil lorecum eosto quostrum ipsuntio bero dolupti aectinv eliquae volupta ectur, que ium qui con non repe vide sit, explignistem et odit verrupta dolupta vent quo cusciisto magnis ma et voleccullam, sandiatur? Quiae qui to dit prestectione sed mod molori ut evenduci volentis res aut aut peres quost asim quis ab in por ratur solorit inciam, offic tem quas ab ium everum, simusda porestiant quam rem reptaectem ratibusda velenis voluptatio et quam utati in reptate vernate perum re, susdaecest ipsaperunti que endi que es modi dis reptam fugiaer eruntorem inullen imintiasit es dolorio volupta tiaepra veles aut voluptur, voles maion nullend ebitem explatur acepedi pictus doloreh enditae. Nisquas nonsedis aut lacimod quia qui aces molo quid etur remodi occumquam dollabori to te int reris doloriatur si beat explant, que pre con conecum rempori quiatendes num voloris ipsunt modipit minvendae litatur? Asitatio etur, que si consed quide vellibe rchille ntionem nime voloriossit, offic te numquibus perrovidus pos volori blaccatur? Biscias il id et evelentene prest landicipis quis aut hil et la aut volupid est est exero bearuntes quosaes ent volest voloreptur mintio ipis doles sum quaspel ibusandam, quatur acerovi tasitiant vellitatis nimus expellaniet volorer orroviducim quibus velent ullatium sapiendant lautem quiandi tatquat.</p>
    <p>Ut dolut et autem dolupicia qui id eosandae in repta que cum etur reptat rerchil lorecum eosto quostrum ipsuntio bero dolupti aectinv eliquae volupta ectur, que ium qui con non repe vide sit, explignistem et odit verrupta dolupta vent quo cusciisto magnis ma et voleccullam, sandiatur? Quiae qui to dit prestectione sed mod molori ut evenduci volentis res aut aut peres quost asim quis ab in por ratur solorit inciam, offic tem quas ab ium everum, simusda porestiant quam rem reptaectem ratibusda velenis voluptatio et quam utati in reptate vernate perum re, susdaecest ipsaperunti que endi que es modi dis reptam fugiaer eruntorem inullen</p>
  </section>

  <p class="signoff">Lab illecta tiumqui consequi dol-<br>oribust molorpo renditio que in<br>conecto este nobis niatemo lup-</p>

  <p class="footer-note">Lab illecta tiumqui consequi doloribust<br>molorpo renditio que in conecto este nobis<br>niatemo luptaerendae etureresete sit atiissus</p>

  <div class="bottom-band"></div>
</main>
</body>
</html>
```